Stylist/Barber Standup Sign for Hair Regrowth Company

We want to design an attractive and eye-catching sign for hair stylists and barbers to sit on their workstations to attract the attention of their clients regarding hair loss and encourage them to speak to their stylist about it of they are would like to seek treatment.
50% of men and 25% of women suffer from hair loss but most are in denial that it is happening or too embarrassed to talk about it.

Copy for the flyer is as follows:

[Section 1:]
This flyer has been placed here/designed to spark conversation about hair loss

[Section 2:]
The truth is...
73% of people believe their hair is thinning
They are right

[Section 3:]
If you've got questions, your stylist or barber has answers.

Additional Background Information:

Primary target audience is men between the ages of 25-45, secondary target audience is men 46-60

Current Consumer Perception? (in the first person) “I’ve been thinking about my hair. I think it’s getting thinner and I’m scared, worried and don’t know what to do. But I don’t know if there is anything that really works. I’ve tried other things and nothing‘s worked.”

Tonality of materials? Very guy friendly, matter of fact, authoritative, its what you might hear from your best friend. Confident. Encouraging, but with a sense of urgency.

Please use our brand colors, but do not include our logo or brand name.
Colors are as follows:
Green: #4ca26f
Light Grey: #999999
Dark Grey: #262626

I have attached print templates in both PDF and Jpeg, please use those to provide final ready to print documents if you are selected.

Target Market(s)

Industry/Entity Type

Health And Wellness

Font styles to use
Sans Serif

Colors
00a990
ffffff
333333
cbcbcb

Requirements
Must have
• We want to get across the following messaging. Ideally you will submit a design using our copy and if you think you can do better, please feel free to submit another design with your own copy/messaging. If you can do it better we would love to select you :-)
• Our copy?
• This flyer has been placed here/designed to spark conversation about hair loss
• The truth is...
• 73% of people believe their hair is thinning
• They are right
• If you've got questions, your stylist or barber has answers
• Also please use our brand colors:
• Green: #4ca26f
• Light Grey: #999999
• Dark Grey: #262626
Should not have
• dont add any logos, images or ornate design. this needs to be simple, easy to ready and eye catching.
• do not use the color red in any capacity.

```html
<!DOCTYPE html>
<html lang="en">
<head>
<meta charset="UTF-8">
<title>Hair Loss Conversation Sign</title>
<link rel="stylesheet" href="https://fonts.googleapis.com/css2?family=Lato:wght@300;400;700;900&display=swap">
<style>
  :root {
    --page-bg: #c4c4c4;
    --sign-top: #5f7687;
    --sign-mid: #7f9aa8;
    --sign-bottom: #b9dde5;
    --text-light: #f1f3f4;
    --text-dark: #262626;
    --highlight-box: #454545;
    --headline: #ececec;
    --placeholder: #c2bcb6;
  }
  * { margin: 0; padding: 0; box-sizing: border-box; }
  html, body {
    width: 1200px;
    height: 960px;
    overflow: hidden;
    background: var(--page-bg);
    font-family: "Lato", Arial, sans-serif;
  }
  .sign {
    position: absolute;
    left: 294px;
    top: 20px;
    width: 612px;
    height: 920px;
    overflow: hidden;
    background: linear-gradient(180deg, var(--sign-top) 0%, var(--sign-mid) 50%, var(--sign-bottom) 100%);
  }
  .intro, .truth {
    position: absolute;
    left: 25px;
    color: var(--text-light);
    font-weight: 300;
    letter-spacing: 0.2px;
  }
  .intro {
    top: 30px;
    font-size: 41px;
    line-height: 52px;
  }
  .truth {
    top: 248px;
    font-size: 38px;
    line-height: 51px;
  }
  .highlight {
    display: inline-block;
    background: var(--highlight-box);
    color: var(--text-light);
    font-weight: 700;
    padding: 0 6px 0 4px;
    margin-left: -3px;
  }
  .highlight--topic {
    font-size: 61px;
    line-height: 57px;
    margin-top: 6px;
  }
  .highlight--stat {
    font-size: 47px;
    line-height: 57px;
    margin: 0 0 2px;
  }
  .headline {
    position: absolute;
    left: 0;
    top: 494px;
    width: 100%;
    text-align: center;
    color: var(--headline);
    font-weight: 700;
    font-size: 75px;
    line-height: 86px;
    letter-spacing: -1.5px;
  }
  .call-to-action {
    position: absolute;
    left: 25px;
    top: 662px;
    color: var(--text-dark);
    font-weight: 400;
    font-size: 35px;
    line-height: 37.5px;
  }
  .photo-area {
    position: absolute;
    left: 262px;
    top: 616px;
    width: 350px;
    height: 304px;
    background: var(--placeholder);
  }
</style>
</head>
<body>
  <main class="sign">
    <p class="intro">
      This flyer has been placed here<br>
      to spark conversation about<br>
      <span class="highlight highlight--topic">hair loss</span>
    </p>

    <p class="truth">
      The truth is...<br>
      <span class="highlight highlight--stat">73% of people</span><br>
      believe their<br>
      hair is thinning
    </p>

    <h1 class="headline">They are right</h1>

    <p class="call-to-action">
      If you've got<br>
      questions,<br>
      your stylist or<br>
      barber has<br>
      answers.
    </p>

    <div class="photo-area" role="img" aria-label="Photo of the top of a bald man's head glancing sideways"></div>
  </main>
</body>
</html>
```